I need a box design created for a DNA Fitness Test

I need a modern and sleek box design for a fitness test. The box needs to have our logo on it and should be clean and modern. The Box is 9 Inches Long 3 and 3/4 inches wide, and 2 inches tall. Company logo attached. The company name is cedar vitality.

Target Market(s)

Fitness

Industry/Entity Type

Fitness

Requirements
Must have
• Our logo

```html
<!DOCTYPE html>
<html lang="en">
<head>
<meta charset="utf-8">
<title>Cedar Vitality – DNA Fitness Test Box</title>
<link rel="stylesheet" href="https://fonts.googleapis.com/css2?family=Montserrat:wght@500;800&display=swap">
<style>
  :root {
    --page-bg: #eef0f2;
    --panel-white: #f3f4f5;
    --panel-edge: #d9dcdf;
    --ink: #141414;
    --ink-soft: #2a2a2a;
    --mark-blue: #2f6fc0;
    --white: #ffffff;
  }
  * { margin: 0; padding: 0; box-sizing: border-box; }
  html, body { width: 1200px; height: 1200px; overflow: hidden; }
  body {
    background: var(--page-bg);
    font-family: "Montserrat", sans-serif;
    position: relative;
  }
  .dieline {
    position: absolute;
    left: 324px;
    top: 72px;
    width: 552px;
    height: 1056px;
  }
  .panel {
    position: absolute;
    background: var(--panel-white);
    border: 1px solid var(--panel-edge);
    overflow: hidden;
  }
  .panel--top   { left: 192px; top: 0;     width: 360px; height: 192px; }
  .panel--side  { left: 0;     top: 192px; width: 192px; height: 864px; }
  .panel--front { left: 192px; top: 192px; width: 360px; height: 864px; }

  .sky { position: absolute; left: 0; top: 0; width: 100%; }
  .panel--top .sky   { height: 100%; }
  .panel--side .sky  { height: 300px; }
  .panel--front .sky { height: 360px; }

  .top-name {
    position: absolute;
    left: 0; right: 0; top: 64px;
    text-align: center;
    color: var(--white);
    line-height: 1;
  }
  .top-name__main { font-weight: 800; font-size: 30px; letter-spacing: 1px; }
  .top-name__sub  { font-weight: 500; font-size: 12px; letter-spacing: 9px; margin-top: 6px; padding-left: 9px; }

  .wordmark {
    position: absolute;
    writing-mode: vertical-rl;
    transform: rotate(180deg);
    color: var(--ink);
    line-height: 1;
    white-space: nowrap;
  }
  .wordmark__main,
  .wordmark__sub { display: block; text-align: center; }
  .wordmark__main { font-weight: 800; }
  .wordmark__sub  { font-weight: 500; color: var(--ink-soft); }

  .panel--front .wordmark { left: 206px; top: 296px; }
  .panel--front .wordmark__main { font-size: 84px; letter-spacing: 2px; }
  .panel--front .wordmark__sub  { font-size: 21px; letter-spacing: 17px; margin-left: 14px; }

  .panel--side .wordmark { left: 60px; top: 290px; }
  .panel--side .wordmark__main { font-size: 56px; letter-spacing: 1px; }
  .panel--side .wordmark__sub  { font-size: 14px; letter-spacing: 11px; margin-left: 8px; }

  .brand-seal {
    position: absolute;
    display: flex;
    align-items: center;
    gap: 8px;
    color: var(--mark-blue);
    font-weight: 800;
    font-size: 13px;
    letter-spacing: 1px;
    text-transform: uppercase;
    white-space: nowrap;
  }
  .brand-seal__dot {
    width: 26px; height: 26px;
    border-radius: 50%;
    background: var(--mark-blue);
  }
  .panel--front .brand-seal { left: 24px; top: 440px; }
  .panel--side .brand-seal  { left: 22px; top: 640px; font-size: 11px; }
  .panel--side .brand-seal__dot { width: 22px; height: 22px; }
</style>
</head>
<body>
  <main class="dieline">
    <section class="panel panel--top">
      <svg class="sky" viewBox="0 0 360 192" preserveAspectRatio="none" role="img" aria-label="Blue brushstroke texture">
        <defs>
          <linearGradient id="sky-top" x1="0" y1="0" x2="1" y2="1">
            <stop offset="0" stop-color="#a9d8f2"/>
            <stop offset="0.5" stop-color="#5bb3e6"/>
            <stop offset="1" stop-color="#2d7fc9"/>
          </linearGradient>
        </defs>
        <rect width="360" height="192" fill="url(#sky-top)"/>
      </svg>
      <div class="top-name">
        <div class="top-name__main">CEDAR</div>
        <div class="top-name__sub">VITALITY</div>
      </div>
    </section>

    <section class="panel panel--side">
      <svg class="sky" viewBox="0 0 192 300" preserveAspectRatio="none" role="img" aria-label="Blue brushstroke texture">
        <defs>
          <linearGradient id="sky-side" x1="0" y1="0" x2="0.6" y2="1">
            <stop offset="0" stop-color="#a9d8f2"/>
            <stop offset="0.55" stop-color="#5bb3e6"/>
            <stop offset="1" stop-color="#2d7fc9"/>
          </linearGradient>
        </defs>
        <path d="M0 0H192V200L178 214L168 196L150 232L132 210L116 250L96 228L78 262L60 236L44 270L28 244L12 280L0 258Z" fill="url(#sky-side)"/>
      </svg>
      <div class="wordmark">
        <span class="wordmark__main">CEDAR</span>
        <span class="wordmark__sub">VITALITY</span>
      </div>
      <div class="brand-seal"><span class="brand-seal__dot"></span>Cedar Vitality</div>
    </section>

    <section class="panel panel--front">
      <svg class="sky" viewBox="0 0 360 360" preserveAspectRatio="none" role="img" aria-label="Blue brushstroke texture">
        <defs>
          <linearGradient id="sky-front" x1="0" y1="0" x2="0.8" y2="1">
            <stop offset="0" stop-color="#a9d8f2"/>
            <stop offset="0.5" stop-color="#5bb3e6"/>
            <stop offset="1" stop-color="#2d7fc9"/>
          </linearGradient>
        </defs>
        <path d="M0 0H360V250L340 232L322 268L300 246L282 290L258 262L236 300L214 270L190 318L168 286L146 330L124 296L100 346L78 304L56 340L36 302L16 332L0 310Z" fill="url(#sky-front)"/>
      </svg>
      <div class="wordmark">
        <span class="wordmark__main">CEDAR</span>
        <span class="wordmark__sub">VITALITY</span>
      </div>
      <div class="brand-seal"><span class="brand-seal__dot"></span>Cedar Vitality</div>
    </section>
  </main>
</body>
</html>
```